Banner Design for Physiotherapy Business

I need a banner designed for a physiotherapy business. The word ‘Physiotherapy’ should be prominent at the top. I’ve attached a document outlining what text and a suggestion of a picture I’d like included. The photo I have suggested in the document won’t upload to plumvista though as the dimensions are too large. I am open to other photos being used though. I would like to see designs that use the colour orange (as seen in the example) or green preferrably. The dimensions need to be 841mm x 2055mm and provided in PDF, JPG, and PNG format and 300dpi in CMYK colour mode.

```html
<!DOCTYPE html>
<html lang="en">
<head>
<meta charset="utf-8">
<title>Physiotherapy Banner</title>
<link rel="stylesheet" href="https://fonts.googleapis.com/css2?family=Bebas+Neue&family=Passion+One:wght@700&family=Montserrat:wght@500;700&family=Roboto:wght@400;500&display=swap">
<style>
  :root {
    --stage: #6d6e71;
    --paper: #ffffff;
    --ink: #1e1a1a;
    --orange: #f26b21;
    --amber: #f7a21b;
    --sun: #fcc419;
    --slate: #555555;
    --guild-blue: #1b8fd6;
    --photo-light: #e7f1f8;
    --photo-mid: #9fc3e0;
  }
  html, body {
    margin: 0;
    width: 1200px;
    height: 1200px;
    overflow: hidden;
    background: var(--stage);
  }
  .stage { display: block; width: 1200px; height: 1200px; }
  .banner-title { font-family: "Bebas Neue", sans-serif; fill: var(--ink); }
  .section-kicker { font-family: "Passion One", sans-serif; font-weight: 700; fill: var(--orange); }
  .section-sub { font-family: "Montserrat", sans-serif; font-weight: 700; fill: var(--slate); }
  .service { font-family: "Montserrat", sans-serif; font-weight: 500; fill: var(--ink); font-size: 21px; }
  .service-note { font-family: "Montserrat", sans-serif; font-weight: 500; fill: var(--ink); font-size: 16px; }
  .bullet { fill: var(--orange); }
  .cta-heading { font-family: "Roboto", sans-serif; font-weight: 500; fill: var(--paper); font-size: 14.5px; letter-spacing: 0.5px; }
  .cta-line { font-family: "Roboto", sans-serif; font-weight: 400; fill: var(--paper); font-size: 14px; }
  .guild-name { font-family: "Roboto", sans-serif; font-weight: 400; fill: var(--guild-blue); }
</style>
</head>
<body>
<svg class="stage" viewBox="0 0 1800 1800" xmlns="http://www.w3.org/2000/svg">
  <defs>
    <clipPath id="banner-clip"><rect width="609" height="1490"/></clipPath>
    <linearGradient id="band-gradient" x1="0" y1="0" x2="1" y2="0.4">
      <stop offset="0" stop-color="#f26b21"/>
      <stop offset="1" stop-color="#fcc419"/>
    </linearGradient>
    <linearGradient id="photo-tone" gradientUnits="userSpaceOnUse" x1="60" y1="170" x2="540" y2="840">
      <stop offset="0" stop-color="#f4f8fb"/>
      <stop offset="0.5" stop-color="#7aa9d6"/>
      <stop offset="1" stop-color="#d9e3ea"/>
    </linearGradient>
    <linearGradient id="ring-photo-tone" x1="0" y1="0" x2="1" y2="1">
      <stop offset="0" stop-color="#e9eef4"/>
      <stop offset="0.55" stop-color="#3e4a9a"/>
      <stop offset="1" stop-color="#4f9c84"/>
    </linearGradient>
    <linearGradient id="cta-sun" x1="0" y1="0" x2="1" y2="0">
      <stop offset="0" stop-color="#fcc419"/>
      <stop offset="1" stop-color="#f7a21b"/>
    </linearGradient>

    <g id="physio-banner">
      <rect class="banner-paper" width="609" height="1490" fill="var(--paper)"/>
      <g clip-path="url(#banner-clip)">
        <!-- header -->
        <text class="banner-title" x="50" y="124" font-size="118" textLength="508" lengthAdjust="spacingAndGlyphs">PHYSIOTHERAPY</text>

        <!-- accent bands -->
        <polygon class="band-left" points="0,182 130,246 130,560 0,498" fill="var(--amber)"/>
        <path class="band-right" d="M380,260 L535,197 Q580,180 580,228 L580,597 L420,520 Z" fill="var(--orange)"/>
        <path class="band-lower" d="M325,790 L609,612 L609,1002 L385,888 Q325,858 325,820 Z" fill="url(#band-gradient)"/>

        <!-- hero photo frame -->
        <path class="hero-frame" d="M76,165 L536,395 L536,840 L76,610 Z" fill="var(--amber)" stroke="var(--amber)" stroke-width="42" stroke-linejoin="round"/>
        <path class="hero-photo" role="img" aria-label="Photo: physiotherapist guiding a senior patient through an arm exercise in a bright clinic" d="M80,178 L526,401 L526,828 L80,605 Z" fill="url(#photo-tone)" stroke="url(#photo-tone)" stroke-width="26" stroke-linejoin="round"/>

        <!-- services -->
        <text class="section-kicker" x="48" y="801" font-size="46">WHAT</text>
        <text class="section-sub" x="49" y="822" font-size="20">WE TREAT / SERVICES</text>

        <g class="service-list">
          <circle class="bullet" cx="48" cy="863" r="3"/><text class="service" x="60" y="870">Arthritis</text>
          <circle class="bullet" cx="48" cy="893" r="3"/><text class="service" x="60" y="900">Back Pain/Neck Pain</text>
          <circle class="bullet" cx="48" cy="923" r="3"/><text class="service" x="60" y="930">Sciatic Pain</text>
          <circle class="bullet" cx="48" cy="953" r="3"/><text class="service" x="60" y="960">Sports Injuries</text>
          <circle class="bullet" cx="48" cy="983" r="3"/><text class="service" x="60" y="990">Repetitive Strain Injuries</text>
          <circle class="bullet" cx="48" cy="1013" r="3"/><text class="service" x="60" y="1020">Post Surgical Management</text>
          <text class="service-note" x="60" y="1039">(Hip And Knee Arthroscopes, Joint Replacement Surgery)</text>
          <circle class="bullet" cx="48" cy="1061" r="3"/><text class="service" x="60" y="1068">Shoulder Pain And Dysfunction</text>
          <circle class="bullet" cx="48" cy="1091" r="3"/><text class="service" x="60" y="1098">Tennis Elbow</text>
          <circle class="bullet" cx="48" cy="1121" r="3"/><text class="service" x="60" y="1128">Postural Pain</text>
          <circle class="bullet" cx="48" cy="1151" r="3"/><text class="service" x="60" y="1158">Workplace Injuries</text>
          <circle class="bullet" cx="48" cy="1181" r="3"/><text class="service" x="60" y="1188">Motor Vehicle Accidents</text>
          <circle class="bullet" cx="48" cy="1211" r="3"/><text class="service" x="60" y="1218">Women’s Health Issues</text>
          <circle class="bullet" cx="48" cy="1241" r="3"/><text class="service" x="60" y="1248">Clinical Exercise</text>
          <circle class="bullet" cx="48" cy="1271" r="3"/><text class="service" x="60" y="1278">Pre-employment Functional</text>
          <text class="service" x="60" y="1299">Assessments</text>
        </g>

        <!-- round photo -->
        <circle class="ring-frame" cx="533" cy="1197" r="128" fill="none" stroke="#f7931e" stroke-width="14"/>
        <circle class="ring-photo" role="img" aria-label="Photo: nurse supporting an elderly woman walking along parallel rehabilitation bars" cx="533" cy="1197" r="116" fill="url(#ring-photo-tone)"/>

        <!-- appointment block -->
        <rect class="cta-sun" x="300" y="1440" width="160" height="80" rx="30" fill="url(#cta-sun)"/>
        <path class="cta-panel" d="M400,1343 L609,1343 L609,1490 L410,1490 L365,1390 Q355,1343 400,1343 Z" fill="var(--orange)"/>
        <text class="cta-heading" x="567" y="1376" text-anchor="end">MAKE AN APPOINTMENT</text>
        <text class="cta-line" x="567" y="1405" text-anchor="end">Brookvale Family Practice</text>
        <text class="cta-line" x="567" y="1422" text-anchor="end">18-20 Elm Rd</text>
        <text class="cta-line" x="567" y="1439" text-anchor="end">Brookvale VIC 3100</text>
        <text class="cta-line" x="567" y="1456" text-anchor="end">(03) 9555 0142</text>

        <!-- membership -->
        <circle class="guild-dot" cx="92" cy="1405" r="38" fill="var(--guild-blue)"/>
        <text class="guild-name" x="167" y="1382" font-size="15">ALLIED MOTION</text>
        <text class="guild-name" x="167" y="1398" font-size="15">GUILD</text>
        <rect class="guild-rule" x="167" y="1417" width="128" height="1.5" fill="var(--guild-blue)"/>
        <text class="guild-name" x="167" y="1443" font-size="22">Member</text>
      </g>
    </g>
  </defs>

  <rect width="1800" height="1800" fill="var(--stage)"/>
  <use href="#physio-banner" x="269" y="155"/>
  <use href="#physio-banner" x="922" y="155"/>
</svg>
</body>
</html>
```